Law Office business card design

I have a general practice specializing in criminal defense work and domestic cases. I have extensive trial and appellate experience.

Target Market(s)

general public

Industry/Entity Type

Defense

Contact Information for Business Card

Darrowby Law Office, P.A.
382 N. 4th
PO Box 5274
Salina, KS 67409-5274
(785) 555-0172
(785) 555-0198 FAX
tdarrow@plinkmail.example

Requirements
Must have
• A symbol that immediately identifes the card as a legal practice.

```html
<!DOCTYPE html>
<html lang="en">
<head>
<meta charset="utf-8">
<title>Darrowby Law Office – Business Card</title>
<link href="https://fonts.googleapis.com/css2?family=Lato:wght@400;700;900&display=swap" rel="stylesheet">
<style>
  :root {
    --backdrop: #e4e4e2;
    --card: #2e2e2f;
    --teal: #2cbaa7;
    --ink-light: #ffffff;
  }
  * { margin: 0; padding: 0; box-sizing: border-box; }
  html, body {
    width: 1200px;
    height: 1000px;
    overflow: hidden;
    background: var(--backdrop);
    font-family: "Lato", Arial, sans-serif;
  }
  .stage {
    width: 1200px;
    height: 1000px;
    display: flex;
    align-items: center;
    justify-content: center;
  }
  .business-card {
    position: relative;
    width: 520px;
    height: 910px;
    background: var(--card);
    box-shadow: 0 10px 30px rgba(0,0,0,0.25);
    overflow: hidden;
  }
  .seal {
    position: absolute;
    top: 70px;
    left: 50%;
    transform: translateX(-50%);
    width: 280px;
    height: 280px;
  }
  .card-text {
    position: absolute;
    left: 48px;
    right: 30px;
    top: 420px;
  }
  .attorney-name {
    color: var(--teal);
    font-weight: 900;
    font-size: 35px;
    letter-spacing: 0.5px;
    text-transform: uppercase;
    white-space: nowrap;
  }
  .firm-name {
    margin-top: 44px;
    color: var(--teal);
    font-weight: 700;
    font-size: 27px;
  }
  .address {
    margin-top: 4px;
    color: var(--ink-light);
    font-size: 25px;
    line-height: 1.3;
  }
  .contact-list {
    margin-top: 40px;
    list-style: none;
    color: var(--ink-light);
    font-size: 25px;
    line-height: 1.35;
  }
  .contact-label { color: var(--teal); }
  .accent-band {
    position: absolute;
    left: 0;
    right: 0;
    bottom: 0;
    height: 38px;
    background: var(--teal);
  }
</style>
</head>
<body>
  <main class="stage">
    <article class="business-card">
      <svg class="seal" viewBox="0 0 280 280" role="img" aria-label="Scales of justice seal emblem">
        <circle cx="140" cy="140" r="138" fill="var(--teal)"/>
        <circle cx="140" cy="140" r="108" fill="var(--card)"/>
      </svg>

      <div class="card-text">
        <h1 class="attorney-name">Theresa A. Darrowby</h1>
        <p class="firm-name">Darrowby Law Office</p>
        <p class="address">382 N. 4th St, PO Box 5274<br>Salina, KS 67409-5274</p>
        <ul class="contact-list">
          <li><span class="contact-label">Telephone:</span> (785) 555-0172</li>
          <li><span class="contact-label">Fax:</span> (785) 555-0198</li>
          <li><span class="contact-label">Email:</span> tdarrow@plinkmail.example</li>
        </ul>
      </div>

      <div class="accent-band"></div>
    </article>
  </main>
</body>
</html>
```